Electrical Product Brochure Design

We have 15 electricians on the road and want to create a product brochure for them to show residential clients. I have attached all the product images in high res to be used and some images of our company and logo. I have also attached a previous product brochure that was designed which we don't want to use/has been edited. Additionally there is a Word document with the content that is needed.

Please create the brochure as a double sided A4 brochure.
Updates

Hi, Thank you for your designs. Please see the updated brief including ensuring the design is a double sided A4 flyer. Please ensure all products from the product brochure content are used on the design and all content. Please ensure Travik's contact information is used as well. Please ensure you see the updated brief for new product images I have now been able to upload as well as a few options for images of our tradespeople that can be used. Thank you.

Target Market(s)

Homeowners

Industry/Entity Type

Electrical

Font styles to use
Sans Serif

Colors
0255a3
fbed22
ec1f27

Requirements
Must have
• Travik colours including mainly blue, but also red and a bit of yellow.
• Travik's contact information including website, phone, email, and PO Box address.
• Each product's image with the content listed next to the image.
Nice to have
• If the four types of fan images could be used, and listed as one product.
• If you could also use images of our tradespeople attached as well?

```html
<!DOCTYPE html>
<html lang="en">
<head>
<meta charset="utf-8">
<title>Travik Electrical Services – Product Flyer</title>
<link href="https://fonts.googleapis.com/css2?family=Open+Sans:wght@400;600;700;800&family=Montserrat:wght@600;700;800&display=swap" rel="stylesheet">
<style>
:root{
  --blue:#0255a3;
  --blue-dark:#023f7a;
  --red:#ec1f27;
  --yellow:#fbed22;
  --paper:#f7f8fa;
  --ink:#2b2f36;
  --muted:#6b7280;
  --backdrop:#d6d7d9;
  --thumb:#e4e7ec;
}
*{box-sizing:border-box;margin:0;padding:0}
html,body{width:791px;height:1200px;overflow:hidden}
body{background:var(--backdrop);font-family:"Open Sans",Arial,sans-serif;color:var(--ink);position:relative}
.page{position:absolute;width:400px;height:566px;background:var(--paper);overflow:hidden;box-shadow:0 6px 18px rgba(0,0,0,.25)}
.page-front{left:150px;top:30px}
.page-back{left:241px;top:614px}

/* front header */
.brand-box{position:absolute;left:14px;top:16px;width:128px;height:42px;border:2px solid var(--blue);background:#fff;display:flex;flex-direction:column;justify-content:center;align-items:center}
.brand-name{font-family:"Montserrat",sans-serif;font-weight:800;font-size:18px;letter-spacing:2px;color:var(--blue);line-height:1}
.brand-sub{font-family:"Montserrat",sans-serif;font-weight:700;font-size:6px;letter-spacing:1px;color:var(--blue);margin-top:3px}
.team-photo{position:absolute;right:0;top:0;width:210px;height:112px;background:linear-gradient(135deg,#c9ced6,#7a8596 60%,#2b3a55)}
.headline{position:absolute;left:14px;top:70px;font-family:"Montserrat",sans-serif;font-weight:800;font-size:15px;line-height:1.1;color:var(--blue)}
.headline em{font-style:normal;color:var(--red)}
.stripe{position:absolute;left:0;width:100%;height:7px;background:var(--blue)}
.stripe::after{content:"";position:absolute;left:0;bottom:-3px;width:100%;height:3px;background:var(--red)}
.front-stripe{top:116px}

/* product card */
.product{position:absolute;width:182px;height:84px}
.thumb{position:absolute;left:0;top:8px;width:54px;height:54px;background:var(--thumb);border:1px solid #cfd4db}
.tag{position:absolute;left:58px;top:0;right:0;height:15px;padding:0 6px;font-family:"Montserrat",sans-serif;font-weight:700;font-size:7px;letter-spacing:.4px;text-transform:uppercase;color:#fff;line-height:15px}
.tag.blue{background:var(--blue)}
.tag.red{background:var(--red)}
.product ul{position:absolute;left:60px;top:20px;right:0;list-style:none}
.product li{font-size:6.3px;line-height:1.55;color:var(--ink);padding-left:7px;position:relative}
.product li::before{content:"";position:absolute;left:0;top:3px;width:3px;height:3px;background:var(--red)}

/* front footer */
.front-footer{position:absolute;left:0;bottom:0;width:100%;height:46px;background:var(--blue)}
.front-footer::before{content:"";position:absolute;left:0;top:-5px;width:100%;height:5px;background:var(--red)}
.footer-info{position:absolute;left:14px;top:10px;font-size:6.5px;color:#fff;line-height:1.6}
.phone-badge{position:absolute;right:14px;top:9px;height:26px;padding:0 12px;background:#fff;border-left:5px solid var(--yellow);display:flex;align-items:center;gap:6px;font-family:"Montserrat",sans-serif;font-weight:800;font-size:13px;color:var(--blue)}
.phone-badge svg{width:12px;height:12px}

/* back header */
.back-header{position:absolute;left:0;top:0;width:100%;height:92px}
.back-header svg{position:absolute;left:0;top:0;width:100%;height:100%}
.back-brand{position:absolute;right:18px;top:20px;text-align:right;color:#fff}
.back-brand .brand-name{color:#fff;font-size:22px}
.back-brand .brand-sub{color:#fff;font-size:8px;margin-top:4px}

/* back contact */
.contact-strip{position:absolute;left:0;top:482px;width:100%;height:84px}
.contact-strip svg{position:absolute;left:0;top:0;width:100%;height:100%}
.contact-list{position:absolute;left:18px;top:30px;font-size:6.5px;line-height:1.7;color:var(--ink)}
.contact-phone{position:absolute;left:200px;top:30px;display:flex;align-items:center;gap:6px;font-family:"Montserrat",sans-serif;font-weight:800;font-size:15px;color:var(--blue)}
.contact-phone svg{width:14px;height:14px;position:static}
</style>
</head>
<body>

<section class="page page-front">
  <div class="brand-box">
    <span class="brand-name">TRAVIK</span>
    <span class="brand-sub">ELECTRICAL SERVICES</span>
  </div>
  <div class="team-photo" role="img" aria-label="Photo of two Travik electricians in navy uniforms"></div>
  <h1 class="headline">CLEVER <em>SOLUTIONS</em><br>FOR YOUR HOME</h1>
  <div class="stripe front-stripe"></div>

  <article class="product" style="left:14px;top:136px">
    <div class="thumb" role="img" aria-label="Photo of smoke alarm"></div>
    <h3 class="tag blue">Smoke Alarms</h3>
    <ul><li>Hardwired with battery backup</li><li>Interconnected for full coverage</li><li>Meets current safety standards</li></ul>
  </article>
  <article class="product" style="left:206px;top:136px">
    <div class="thumb" role="img" aria-label="Photo of ceiling fan range"></div>
    <h3 class="tag red">Ceiling Fans</h3>
    <ul><li>Four modern styles available</li><li>Quiet and energy efficient</li><li>Optional light and remote</li></ul>
  </article>
  <article class="product" style="left:14px;top:228px">
    <div class="thumb" role="img" aria-label="Photo of USB power point"></div>
    <h3 class="tag red">USB Power Points</h3>
    <ul><li>Charge devices without adaptors</li><li>Slim white wall finish</li><li>Double outlet with USB</li></ul>
  </article>
  <article class="product" style="left:206px;top:228px">
    <div class="thumb" role="img" aria-label="Photo of sensor light"></div>
    <h3 class="tag blue">Sensor Lights</h3>
    <ul><li>Motion activated LED lighting</li><li>Ideal for entries and driveways</li><li>Weatherproof outdoor rating</li></ul>
  </article>
  <article class="product" style="left:14px;top:320px">
    <div class="thumb" role="img" aria-label="Photo of LED downlight"></div>
    <h3 class="tag blue">LED Downlights</h3>
    <ul><li>Cuts lighting costs significantly</li><li>Long life low heat</li><li>Warm or cool options</li></ul>
  </article>
  <article class="product" style="left:206px;top:320px">
    <div class="thumb" role="img" aria-label="Photo of exhaust fan"></div>
    <h3 class="tag red">Exhaust Fans</h3>
    <ul><li>Removes steam and odours</li><li>Helps prevent mould growth</li><li>Quiet ducted installation</li></ul>
  </article>
  <article class="product" style="left:14px;top:412px">
    <div class="thumb" role="img" aria-label="Photo of surge protector"></div>
    <h3 class="tag red">Surge Protection</h3>
    <ul><li>Protects valuable home electronics</li><li>Fitted at the switchboard</li><li>Guards against power spikes</li></ul>
  </article>
  <article class="product" style="left:206px;top:412px">
    <div class="thumb" role="img" aria-label="Photo of safety switch"></div>
    <h3 class="tag blue">Safety Switches</h3>
    <ul><li>Cuts power in milliseconds</li><li>Protects your whole family</li><li>Tested and certified install</li></ul>
  </article>

  <footer class="front-footer">
    <p class="footer-info">www.travikelectrical.com.au<br>PO Box 512, Riverwood NSW 2210</p>
    <div class="phone-badge">
      <svg viewBox="0 0 24 24"><path fill="#0255a3" d="M6.6 10.8a15.1 15.1 0 0 0 6.6 6.6l2.2-2.2a1 1 0 0 1 1-.25 11.4 11.4 0 0 0 3.6.57 1 1 0 0 1 1 1V20a1 1 0 0 1-1 1A17 17 0 0 1 3 4a1 1 0 0 1 1-1h3.5a1 1 0 0 1 1 1c0 1.25.2 2.45.57 3.57a1 1 0 0 1-.25 1z"/></svg>
      02 5550 1847
    </div>
  </footer>
</section>

<section class="page page-back">
  <div class="back-header">
    <svg viewBox="0 0 400 92" preserveAspectRatio="none">
      <polygon points="0,0 400,0 400,62 0,88" fill="#0255a3"/>
      <polygon points="0,88 400,62 400,68 0,94" fill="#ec1f27"/>
    </svg>
    <div class="back-brand">
      <span class="brand-name">TRAVIK</span><br>
      <span class="brand-sub">ELECTRICAL SERVICES</span>
    </div>
  </div>

  <article class="product" style="left:14px;top:104px">
    <div class="thumb" role="img" aria-label="Photo of pendant lights"></div>
    <h3 class="tag blue">Pendant Lighting</h3>
    <ul><li>Stylish kitchen feature lighting</li><li>Range of modern shades</li><li>Dimmable on request</li></ul>
  </article>
  <article class="product" style="left:206px;top:104px">
    <div class="thumb" role="img" aria-label="Photo of outdoor garden lights"></div>
    <h3 class="tag red">Garden Lighting</h3>
    <ul><li>Highlights paths and plants</li><li>Low voltage LED fittings</li><li>Timer or sensor control</li></ul>
  </article>
  <article class="product" style="left:14px;top:196px">
    <div class="thumb" role="img" aria-label="Photo of data point"></div>
    <h3 class="tag red">Data Points</h3>
    <ul><li>Fast reliable wired internet</li><li>Ideal for home offices</li><li>Neat wall plate finish</li></ul>
  </article>
  <article class="product" style="left:206px;top:196px">
    <div class="thumb" role="img" aria-label="Photo of TV antenna"></div>
    <h3 class="tag blue">TV Antennas</h3>
    <ul><li>Clear digital reception</li><li>Extra TV points added</li><li>Signal testing included</li></ul>
  </article>
  <article class="product" style="left:14px;top:288px">
    <div class="thumb" role="img" aria-label="Photo of bathroom heat lamp"></div>
    <h3 class="tag blue">Bathroom Heaters</h3>
    <ul><li>Three in one heat units</li><li>Light fan and warmth</li><li>Comfort through winter months</li></ul>
  </article>
  <article class="product" style="left:206px;top:288px">
    <div class="thumb" role="img" aria-label="Photo of security floodlight"></div>
    <h3 class="tag red">Security Lights</h3>
    <ul><li>Bright LED flood coverage</li><li>Deters unwanted visitors</li><li>Low running costs</li></ul>
  </article>
  <article class="product" style="left:14px;top:380px">
    <div class="thumb" role="img" aria-label="Photo of switchboard"></div>
    <h3 class="tag red">Switchboard Upgrades</h3>
    <ul><li>Replaces old ceramic fuses</li><li>Room for new circuits</li><li>Safer modern protection</li></ul>
  </article>
  <article class="product" style="left:206px;top:380px">
    <div class="thumb" role="img" aria-label="Photo of hot water system"></div>
    <h3 class="tag blue">Hot Water Systems</h3>
    <ul><li>Efficient electric heat pumps</li><li>Sized to your household</li><li>Fast same day install</li></ul>
  </article>

  <div class="contact-strip">
    <svg viewBox="0 0 400 84" preserveAspectRatio="none">
      <polygon points="0,14 400,0 400,6 0,20" fill="#0255a3"/>
      <polygon points="0,78 400,72 400,84 0,84" fill="#ec1f27"/>
    </svg>
    <p class="contact-list">info@travikelectrical.com.au<br>www.travikelectrical.com.au<br>PO Box 512, Riverwood NSW 2210</p>
    <div class="contact-phone">
      <svg viewBox="0 0 24 24"><path fill="#ec1f27" d="M6.6 10.8a15.1 15.1 0 0 0 6.6 6.6l2.2-2.2a1 1 0 0 1 1-.25 11.4 11.4 0 0 0 3.6.57 1 1 0 0 1 1 1V20a1 1 0 0 1-1 1A17 17 0 0 1 3 4a1 1 0 0 1 1-1h3.5a1 1 0 0 1 1 1c0 1.25.2 2.45.57 3.57a1 1 0 0 1-.25 1z"/></svg>
      02 5550 1847
    </div>
  </div>
</section>

</body>
</html>
```